Corbrook Estates LLC stationary for a real estate property management company.

Create stationary (letterhead, envelopes, business cards) using Corbrook Estates LLC logo as primary creative element. Stationary design needs to be horizontal, leaving as much space as possible for correspondence copy. See attached Creative Brief and past stationary files for details.

Target Market(s)

Prospective apartment residents and current residents, vendors, and government agencies.

Industry/Entity Type

Property Management

Contact Information for Business Card

Business card employee title: Property Manager. Should include address, phone, fax, email, website, slogan, and Corbrook Estates logo.

Font styles to use
Sans Serif

Colors
0592cd
000000

Requirements
Must have
• Tone should be conservative, institutional, business (i.e. banking, finance, real estate). Must include: address, phone, fax, website, and slogan (see attached Creative Brief). Should be a horizontal design, leaving as much room as possible for letter correspondence copy.
Nice to have
• Please use an Arial or Helvetica style font.
Should not have
• Letterhead layout should leave as much room as possible for copy.

```html
<!DOCTYPE html>
<html lang="en">
<head>
<meta charset="utf-8">
<title>Corbrook Estates LLC — Stationery</title>
<link href="https://fonts.googleapis.com/css2?family=Arimo:wght@400;700&family=PT+Sans:wght@400&display=swap" rel="stylesheet">
<style>
  :root {
    --backdrop: #cdc2b3;
    --paper: #f5f5f5;
    --paper-edge: #e4e4e4;
    --brand-blue: #0a6cb0;
    --flap-blue: #1170b4;
    --card-deep: #0b2350;
    --card-mid: #1c4d92;
    --card-disc: #c9c3b6;
    --ink: #3a3a3a;
    --ink-soft: #555;
    --white: #ffffff;
  }
  * { box-sizing: border-box; margin: 0; padding: 0; }
  html, body { width: 1200px; height: 754px; overflow: hidden; }
  body {
    position: relative;
    background: var(--backdrop);
    font-family: "Arimo", Arial, sans-serif;
    color: var(--ink);
  }
  .sheet {
    position: absolute;
    background: var(--paper);
    box-shadow: 0 2px 8px rgba(0,0,0,.25);
  }

  /* Brand name wordmark */
  .brand {
    display: flex; align-items: center; gap: 7px;
    color: var(--brand-blue);
    font-weight: 700;
    font-size: 15px;
    line-height: 1.05;
  }
  .brand-dot {
    width: 14px; height: 14px; border-radius: 50%;
    background: var(--brand-blue); flex: none;
  }

  .contact-list { list-style: none; font-size: 8px; line-height: 10px; color: var(--ink); }
  .contact-list li { display: flex; align-items: center; gap: 5px; }
  .contact-list svg { width: 8px; height: 8px; fill: var(--brand-blue); flex: none; }
  .address { font-size: 8px; line-height: 9.5px; margin-bottom: 4px; }

  /* Letterhead */
  .letterhead { left: 36px; top: 32px; width: 489px; height: 690px; }
  .letterhead .brand { position: absolute; left: 46px; top: 58px; width: 170px; font-size: 16px; }
  .letterhead .brand-dot { width: 18px; height: 18px; }
  .letterhead-contact {
    position: absolute; left: 316px; top: 45px; height: 65px;
    border-left: 1px solid #bbb; padding-left: 11px; padding-top: 3px;
  }
  .letter {
    position: absolute; left: 49px; top: 194px; width: 394px;
    font-family: "PT Sans", "Myriad Pro", sans-serif;
  }
  .salutation { font-size: 13px; color: var(--ink-soft); margin-bottom: 24px; }
  .letter p { font-size: 7.4px; line-height: 11.7px; color: var(--ink); margin-bottom: 11.7px; text-align: justify; }
  .closing { font-size: 7.4px; margin-top: 22px; }
  .signature {
    width: 64px; height: 26px; margin-top: 8px;
    background: linear-gradient(90deg, rgba(40,40,60,.08), rgba(40,40,60,.18), rgba(40,40,60,.05));
    border-radius: 4px;
  }

  /* Business card */
  .card {
    position: absolute; left: 717px; top: 106px; width: 313px; height: 178px;
    overflow: hidden;
    background: linear-gradient(100deg, var(--card-deep) 0%, var(--card-mid) 55%, #2c4c7a 100%);
    box-shadow: 0 1px 4px rgba(0,0,0,.25);
  }
  .card-disc { position: absolute; left: 0; top: 0; }
  .card-person { position: absolute; left: 12px; top: 45px; color: var(--white); }
  .card-name { font-size: 11.5px; font-weight: 700; letter-spacing: .2px; }
  .card-title { font-size: 8px; color: #cdd8ea; margin-bottom: 10px; }
  .card-person .address, .card-person .contact-list { color: #dfe7f3; font-size: 7.4px; line-height: 10px; }
  .card-person .address { margin-bottom: 6px; }
  .card-person .contact-list svg { fill: #dfe7f3; }
  .card .brand { position: absolute; left: 165px; top: 83px; width: 135px; font-size: 13px; color: var(--card-deep); }
  .card .brand-dot { background: var(--card-deep); width: 13px; height: 13px; }

  /* Envelope back with flap */
  .envelope-back { left: 615px; top: 350px; width: 549px; height: 248px; background: #ececec; }
  .flap { position: absolute; left: 0; top: 0; }
  .flap-brand {
    position: absolute; left: 0; right: 0; top: 26px; text-align: center;
    color: var(--white); font-size: 8px;
  }
  .flap-brand .brand { color: var(--white); justify-content: center; font-size: 12px; margin-bottom: 6px; }
  .flap-brand .brand-dot { background: var(--white); width: 11px; height: 11px; }

  /* Envelope front */
  .envelope-front { left: 547px; top: 471px; width: 551px; height: 251px; }
  .envelope-front .brand { position: absolute; left: 23px; top: 28px; width: 160px; font-size: 15px; }
  .envelope-front .address { position: absolute; left: 38px; top: 68px; font-size: 8px; }
</style>
</head>
<body>

<svg width="0" height="0" style="position:absolute" aria-hidden="true">
  <symbol id="icon-phone" viewBox="0 0 10 10"><path d="M2 0.5 3.6 2.6 2.8 3.6Q3.8 5.6 6.2 7.1L7.3 6.3 9.5 7.8 8.6 9.4Q4.6 9.2 0.9 4.4 0.4 2 2 0.5Z"/></symbol>
  <symbol id="icon-fax" viewBox="0 0 10 10"><rect x="2.5" y="0.5" width="5" height="3"/><rect x="0.5" y="3.5" width="9" height="4.5" rx="1"/><rect x="2.5" y="7" width="5" height="2.5"/></symbol>
  <symbol id="icon-mail" viewBox="0 0 10 10"><path d="M0.5 2h9v6h-9z M0.5 2 5 5.5 9.5 2"/></symbol>
  <symbol id="icon-web" viewBox="0 0 10 10"><circle cx="5" cy="5" r="4.5"/></symbol>
</svg>

<!-- Letterhead -->
<section class="sheet letterhead">
  <div class="brand"><span class="brand-dot"></span><span>Corbrook Estates LLC</span></div>
  <div class="letterhead-contact">
    <p class="address">1820 Alder Creek Road #B210<br>Fairview, CA 90410</p>
    <ul class="contact-list">
      <li><svg><use href="#icon-phone"/></svg>555-014-2286</li>
      <li><svg><use href="#icon-fax"/></svg>555-014-7731</li>
      <li><svg><use href="#icon-mail"/></svg>dana@corbrookestates.us</li>
      <li><svg><use href="#icon-web"/></svg>www.corbrookestates.us</li>
    </ul>
  </div>
  <article class="letter">
    <p class="salutation">Dear Mr. Hale,</p>
    <p>Lorem ipsum dolor sit amet, consectetur adipiscing elit. Donec orci purus, luctus vitae dignissim eu, iaculis sed purus. Vivamus faucibus, ipsum nec aliquet viverra, leo mauris condimentum ligula, sit amet sagittis enim ligula quis arcu. Nam egestas tortor id nisi porttitor mattis. In tortor ante, ultricies in suscipit a, tempus non massa. Vivamus et auctor mi. Fusce vel massa nulla. Phasellus nec eros mauris, et scelerisque orci.</p>
    <p>Donec malesuada orci vitae nulla accumsan porta a id massa. Quisque accumsan iaculis magna sit amet fringilla. Maecenas consequat, magna eget tincidunt semper, odio nibh rutrum mi, id feugiat ante nisi eu risus. Vestibulum nunc orci, rhoncus a placerat in, ultricies in mi. Cras mattis varius eros, vel fringilla nisi suscipit eget. Quisque scelerisque sagittis nulla at porttitor.</p>
    <p>Sed id augue vitae urna euismod commodo aliquet a quam. Pellentesque arcu velit, cursus et malesuada ut, consequat et diam. Nullam erat sem, rhoncus id ullamcorper vitae, rhoncus et arcu. In ultricies ultricies nulla, ut rutrum nisi iaculis at. Donec eu magna a metus ornare faucibus. Fusce aliquet faucibus ultricies. Morbi semper, est id tincidunt gravida, sem arcu adipiscing lacus, ac bibendum nulla leo eu purus. Quisque nec diam sed risus consectetur a accumsan quis quis nibh. Vestibulum id purus lorem.</p>
    <p>It is a long established fact that a reader will be distracted by the readable content of a page when looking at its layout. The point of using Lorem Ipsum is that it has a more-or-less normal distribution of letters, as opposed to using 'Content here, content here', making it look like readable English. Many desktop publishing packages</p>
    <p class="closing">Sincerely,</p>
    <div class="signature" role="img" aria-label="Handwritten signature"></div>
  </article>
</section>

<!-- Business card -->
<section class="card">
  <svg class="card-disc" width="313" height="178" aria-hidden="true">
    <circle cx="237" cy="94" r="100" fill="var(--card-disc)"/>
  </svg>
  <div class="card-person">
    <p class="card-name">DANA WHITFIELD</p>
    <p class="card-title">Property Manager</p>
    <p class="address">1820 Alder Creek Road #B210<br>Fairview, CA 90410</p>
    <ul class="contact-list">
      <li><svg><use href="#icon-phone"/></svg>555-014-2286</li>
      <li><svg><use href="#icon-fax"/></svg>555-014-7731</li>
      <li><svg><use href="#icon-mail"/></svg>dana@corbrookestates.us</li>
      <li><svg><use href="#icon-web"/></svg>www.corbrookestates.us</li>
    </ul>
  </div>
  <div class="brand"><span class="brand-dot"></span><span>Corbrook Estates LLC</span></div>
</section>

<!-- Envelope back -->
<section class="sheet envelope-back">
  <svg class="flap" width="549" height="92" aria-hidden="true">
    <path d="M0 0H549L538 62Q533 91 505 91H44Q16 91 11 62Z" fill="var(--flap-blue)"/>
  </svg>
  <div class="flap-brand">
    <div class="brand"><span class="brand-dot"></span><span>Corbrook Estates LLC</span></div>
    <p>www.corbrookestates.us</p>
  </div>
</section>

<!-- Envelope front -->
<section class="sheet envelope-front">
  <div class="brand"><span class="brand-dot"></span><span>Corbrook Estates LLC</span></div>
  <p class="address">1820 Alder Creek Road #B210<br>Fairview, CA 90410</p>
</section>

</body>
</html>
```